Lantern Hour book needs a cover design

I need a front and back cover design that demonstrates a strong sense of possibility that trust can be repaired even if things look bleak. Repairing trust is difficult, but this book is full of wisdom, proven strategies, and doctoral research to help people strengthen relationships and improve trust. It can help any group: business, nonprofit, education, service. Showing diversity of groups and people is very important. For the cover title, there should be a play on words: "Lantern Hour: Is it? Possible" should have the words "is it?" crossed out and the words "It IS! should be replaced there in a striking way. Perhaps in red ink. For publishing purposes, book will be titled Lantern Hour: It IS Possible! Please see the attachment for an example. The book layout is approximately 260 pages.

Target Market(s)

A business self-help book, but the target is any person in a group that feels they have lost trust in each other. It can be just a normal person struggling in a volunteer group they are a part of, or a supervisor whose group is not working well together. It can be a leader who just wants their group to be stronger.

Industry/Entity Type

Business Management

Font styles to use
Other font styles liked:
• Allise - I believe is being used on the interior of the book for the title page and headings

Requirements
Must have
• Show hope and possibility in the midst of difficulty. Must have a play on the words in the title "Lantern Hour: Is it? Possible" with crossing out "is it?" with "It IS!" (see attached example) Must include the author's name: Marla Quinby, PhD Must include a smaller tagline: "Proven Strategies to Help Groups Get Unstuck"
Nice to have
• Showing diverse people, or hands. Diverse kinds of groups - not just business. A colorful cover. Maybe show the complexity of trust when it is broken...broken pieces of trust that are then picked up and put together when people work together. Could show people (or images of hands) or other ways to show that it's a choice and it is possible to repair broken trust. I'd also like to convey a sense of a group - not just random people. That they have something at stake to work on repairing trust together and this book can help them.
Should not have
• If images of people are used, just showing one gender or race is not okay. Nor just binary choices: like an image containing one man and one woman, or one white person and one person of color - otherwise it seems that the book on Lantern Hour is about race or gender relations.

```html
<!DOCTYPE html>
<html lang="en">
<head>
<meta charset="utf-8">
<title>Lantern Hour: It IS Possible! — Book Cover</title>
<link rel="stylesheet" href="https://fonts.googleapis.com/css2?family=Bebas+Neue&family=Caveat+Brush&family=Oswald:wght@400;600&display=swap">
<style>
  :root {
    --sand-light: #e3954f;
    --sand-mid: #d0803c;
    --sand-deep: #bb6a2e;
    --carve-dark: #6e3512;
    --carve-face: #c9773a;
    --carve-edge: #f0ae6c;
    --script-ink: #7a3c14;
    --red-ink: #c8141c;
    --white: #ffffff;
  }
  * { margin: 0; padding: 0; box-sizing: border-box; }
  html, body { width: 803px; height: 1200px; overflow: hidden; background: var(--sand-mid); }
  .cover {
    position: relative;
    width: 803px;
    height: 1200px;
    overflow: hidden;
  }
  .sand-backdrop {
    position: absolute;
    inset: 0;
    background: linear-gradient(160deg, var(--sand-light) 0%, var(--sand-mid) 50%, var(--sand-deep) 100%);
  }
  .title {
    position: absolute;
    left: 0;
    top: 80px;
    width: 803px;
    height: 460px;
  }
  .title text {
    font-family: "Bebas Neue", "Oswald", sans-serif;
    fill: var(--carve-face);
    stroke: var(--carve-dark);
    stroke-width: 6;
    paint-order: stroke;
    filter: drop-shadow(-2px -2px 0 var(--carve-dark)) drop-shadow(2px 2px 0 var(--carve-edge));
  }
  .wordplay {
    position: absolute;
    left: 200px;
    top: 560px;
    width: 400px;
    height: 290px;
  }
  .wordplay text {
    font-family: "Caveat Brush", cursive;
    fill: var(--script-ink);
    filter: drop-shadow(1px 1px 0 var(--carve-edge));
  }
  .wordplay .correction { fill: var(--red-ink); filter: none; }
  .wordplay .strike { stroke: var(--script-ink); stroke-width: 6; stroke-linecap: round; }
  .tagline {
    position: absolute;
    left: 0;
    top: 880px;
    width: 803px;
    text-align: center;
    font-family: "Oswald", sans-serif;
    font-weight: 400;
    font-style: italic;
    font-size: 53px;
    line-height: 62px;
    color: var(--white);
    text-transform: uppercase;
    letter-spacing: 0.5px;
  }
  .author {
    position: absolute;
    left: 0;
    top: 1034px;
    width: 803px;
    text-align: center;
    font-family: "Oswald", sans-serif;
    font-weight: 600;
    font-size: 36px;
    color: var(--white);
  }
  .publisher {
    position: absolute;
    left: 0;
    top: 1120px;
    width: 803px;
    display: flex;
    justify-content: center;
    align-items: center;
    gap: 12px;
  }
  .publisher-square { width: 48px; height: 48px; background: var(--white); }
  .publisher-name {
    font-family: "Oswald", sans-serif;
    font-weight: 400;
    font-size: 24px;
    line-height: 25px;
    letter-spacing: 2px;
    color: var(--white);
    text-transform: uppercase;
  }
</style>
</head>
<body>
<main class="cover">
  <div class="sand-backdrop" role="img" aria-label="Wind-rippled orange desert sand"></div>

  <svg class="title" viewBox="0 0 803 460" aria-labelledby="title-text">
    <title id="title-text">Lantern Hour</title>
    <text x="110" y="225" textLength="590" lengthAdjust="spacingAndGlyphs" font-size="292">LANTERN</text>
    <text x="120" y="430" textLength="570" lengthAdjust="spacingAndGlyphs" font-size="256">HOUR</text>
  </svg>

  <svg class="wordplay" viewBox="0 0 400 290" aria-label="Is it? crossed out, replaced by It IS Possible!">
    <text class="correction" x="110" y="72" font-size="64">It IS</text>
    <text x="105" y="150" font-size="62">Is it</text>
    <line class="strike" x1="25" y1="108" x2="335" y2="152"/>
    <line class="strike" x1="35" y1="154" x2="340" y2="110"/>
    <line class="strike" x1="20" y1="132" x2="345" y2="130"/>
    <text x="20" y="265" font-size="112" textLength="345" lengthAdjust="spacingAndGlyphs">Possible!</text>
  </svg>

  <p class="tagline">Proven Strategies to Help<br>Groups Get Unstuck</p>

  <p class="author">Marla Quinby. PH.D.</p>

  <div class="publisher">
    <span class="publisher-square"></span>
    <span class="publisher-name">Northgate<br>Press</span>
  </div>
</main>
</body>
</html>
```